Chicago Train Advertisement for HomeAlongRail.com.

We have purchased one month of advertising on the Chicago NRX subway train. We will have 150 cards up in the subway to advertise our website HomeAlongRail.com where people can search for properties by train station. The cards are 11" tall and 46.5" long. We want people to feel compelled to jump on their cell phones and conduct a search for an apartment or home while they are riding the train, or at least enter their email and search criteria so one of our agents can help them.

Target Market(s)

People who want to live near train stations

Industry/Entity Type

Real Estate

Font styles to use
Sans Serif

Colors

Designer to choose colors to be used in the design.

Requirements
Must have
• The homealongrail logo and a catchy slogan, something like: Find your home near a train station the easy way: www.homealongrail.com. Search real estate listings near the NRX or Vorlo.

```html
<!DOCTYPE html>
<html lang="en">
<head>
<meta charset="utf-8">
<title>HomeAlongRail.com Train Card</title>
<link href="https://fonts.googleapis.com/css2?family=Montserrat:wght@300;400;700&family=Arimo:wght@400&display=swap" rel="stylesheet">
<style>
  :root {
    --page: #ffffff;
    --band-top: #2c3c9e;
    --band-mid: #3a64c4;
    --band-bottom: #4a8fdc;
    --gold: #f5b92a;
    --white: #ffffff;
    --bar-top: #eef3fa;
    --bar-bottom: #d3dff0;
    --field-border: #4a86d6;
    --ink: #1c1c1c;
    --icon-grey: #9aa3ad;
    --brand-blue: #2f6fc4;
    --go-green: #3cae3a;
  }
  * { box-sizing: border-box; margin: 0; padding: 0; }
  html, body { width: 1200px; height: 1200px; overflow: hidden; background: var(--page); }

  .train-card {
    position: absolute;
    left: 40px; top: 467px;
    width: 1120px; height: 265px;
    box-shadow: 0 4px 10px rgba(0,0,0,0.35);
    overflow: hidden;
  }
  .headline-band {
    position: absolute; left: 0; top: 0; width: 100%; height: 140px;
    background: linear-gradient(180deg, var(--band-top) 0%, var(--band-mid) 55%, var(--band-bottom) 100%);
  }
  .headline {
    position: absolute; left: 48px; top: 22px;
    font-family: 'Montserrat', sans-serif;
    color: var(--white);
    font-size: 42px; line-height: 56px;
    letter-spacing: 3px;
    font-weight: 300;
    text-transform: uppercase;
  }
  .headline strong { color: var(--gold); font-weight: 700; }

  .brand-plate {
    position: absolute; left: 748px; top: 25px;
    width: 372px; height: 63px;
    background: linear-gradient(180deg, #ffffff 0%, #e9eef5 100%);
    display: flex; align-items: center; justify-content: center; gap: 14px;
  }
  .brand-dot { width: 26px; height: 26px; border-radius: 50%; background: var(--brand-blue); }
  .brand-name {
    font-family: 'Montserrat', sans-serif; font-weight: 400;
    font-size: 30px; color: var(--brand-blue);
  }
  .brand-tagline {
    position: absolute; left: 748px; top: 102px; width: 372px;
    text-align: center;
    font-family: 'Montserrat', sans-serif; font-size: 12px;
    letter-spacing: 6px; color: var(--white); text-transform: uppercase;
  }

  .browser-bar {
    position: absolute; left: 0; top: 140px; width: 100%; height: 125px;
    background: linear-gradient(180deg, var(--bar-top) 0%, var(--bar-bottom) 100%);
  }
  .address-field {
    position: absolute; left: 116px; top: 32px;
    width: 954px; height: 58px;
    background: var(--white);
    border: 2px solid var(--field-border);
    border-radius: 3px;
  }
  .back-button {
    position: absolute; left: 51px; top: 23px;
    width: 76px; height: 76px; border-radius: 50%;
    background: linear-gradient(180deg, #ffffff, #e4e9f0);
    border: 2px solid #c6ced9;
  }
  .back-button svg { position: absolute; left: 20px; top: 20px; }
  .info-icon { position: absolute; left: 36px; top: 14px; }
  .url-text {
    position: absolute; left: 86px; top: 9px;
    font-family: 'Arimo', sans-serif; font-size: 33px; color: var(--ink);
  }
  .url-text::after {
    content: ""; display: inline-block; width: 2px; height: 32px;
    background: #444; margin-left: 10px; vertical-align: -5px;
  }
  .dropdown-icon { position: absolute; left: 822px; top: 20px; }
  .field-divider { position: absolute; left: 866px; top: 8px; width: 1px; height: 40px; background: #ccd3dc; }
  .go-arrow { position: absolute; left: 890px; top: 13px; }
  .pointer { position: absolute; left: 1072px; top: 78px; }
</style>
</head>
<body>
  <section class="train-card">
    <div class="headline-band">
      <h1 class="headline">One <strong>Click</strong><br>Find your <strong>Dream Home</strong></h1>
      <div class="brand-plate">
        <span class="brand-dot"></span>
        <span class="brand-name">Wrenfield Realty</span>
      </div>
      <p class="brand-tagline">Search Chicagoland Listings</p>
    </div>

    <div class="browser-bar">
      <div class="back-button">
        <svg width="32" height="32" viewBox="0 0 32 32"><path d="M26 16H8M16 7l-9 9 9 9" fill="none" stroke="#8d969f" stroke-width="4" stroke-linecap="round" stroke-linejoin="round"/></svg>
      </div>
      <div class="address-field">
        <svg class="info-icon" width="28" height="28" viewBox="0 0 28 28"><circle cx="14" cy="14" r="12" fill="none" stroke="#a8b0b9" stroke-width="2"/><rect x="12.8" y="12" width="2.4" height="9" fill="#a8b0b9"/><circle cx="14" cy="8.5" r="1.6" fill="#a8b0b9"/></svg>
        <span class="url-text">HomeAlongRail.com</span>
        <svg class="dropdown-icon" width="26" height="16" viewBox="0 0 26 16"><path d="M1 1h24L13 15z" fill="#e6e9ee" stroke="#b5bcc5" stroke-width="1.5"/></svg>
        <span class="field-divider"></span>
        <svg class="go-arrow" width="32" height="30" viewBox="0 0 32 30"><path d="M2 15h24M15 3l12 12-12 12" fill="none" stroke="var(--go-green)" stroke-width="6" stroke-linejoin="round"/></svg>
      </div>
      <svg class="pointer" width="30" height="40" viewBox="0 0 30 40"><path d="M2 2v30l8-7 6 13 5-2-6-13h11z" fill="#ffffff" stroke="#111" stroke-width="2" stroke-linejoin="round"/></svg>
    </div>
  </section>
</body>
</html>
```